Helicopter scenic /Charter company

Need a sign 920mm x 920mm for our Westbrook Helipad fence that catches the eye for people walking past. Some photos have been attached but feel free to use helicopter photos you have as well. Like the sign to be black with lettering that stands out. You may do a design with photos or it may look better without. It is up to you. It just has to look eye catching and exciting.
Text: Helicopter Joy Flights & Scenic Tours here seven days from October to March. Prices from just $99 per person* Details at skyquilla.com.au or ph 9627 3105
* $99 flights are shared 8 minute flights and are only available on weekends

Target Market(s)

Tourists locals walking past the helipad

Requirements
Must have
• Logo
• Text as in project description

```html
<!DOCTYPE html>
<html lang="en">
<head>
<meta charset="utf-8">
<title>Skyquilla Helicopters – Joy Flights Sign</title>
<link rel="stylesheet" href="https://fonts.googleapis.com/css2?family=Russo+One&family=Fira+Sans:wght@400;500;600;800&family=Arimo&display=swap">
<style>
  :root {
    --brand-blue: #0b72bf;
    --deep-blue: #0a4fa6;
    --sky-top: #3c9ee0;
    --sky-low: #a9d6f4;
    --charcoal: #343436;
    --yellow: #ffd500;
    --white: #ffffff;
    --logo-grey: #bdbdbf;
    --heli-red: #e2232b;
  }
  html, body {
    margin: 0;
    padding: 0;
    width: 1200px;
    height: 1200px;
    overflow: hidden;
    background: #8a8a8c;
  }
  .sign {
    position: relative;
    width: 1200px;
    height: 1200px;
    overflow: hidden;
    font-family: "Fira Sans", sans-serif;
    background: linear-gradient(180deg, var(--sky-top) 0%, #63b5ea 55%, var(--sky-low) 100%);
  }
  .sign__shapes {
    position: absolute;
    inset: 0;
  }
  .heli-photo {
    position: absolute;
    left: 470px;
    top: 580px;
    width: 730px;
    height: 390px;
    background: radial-gradient(ellipse 45% 42% at 55% 52%, rgba(226,35,43,0.95) 0%, rgba(226,35,43,0.75) 45%, rgba(226,35,43,0) 100%);
  }
  .headline {
    position: absolute;
    left: 70px;
    top: 48px;
    margin: 0;
    font-family: "Russo One", sans-serif;
    font-weight: 400;
    color: var(--yellow);
    font-size: 86px;
    line-height: 128px;
    letter-spacing: -1px;
  }
  .season-banner {
    position: absolute;
    left: 125px;
    top: 424px;
    width: 950px;
    height: 131px;
  }
  .season-banner svg { position: absolute; inset: 0; }
  .season-banner__text {
    position: absolute;
    inset: 0;
    display: flex;
    align-items: center;
    justify-content: center;
    gap: 0;
    color: var(--white);
    font-size: 47px;
    font-weight: 400;
    white-space: nowrap;
    padding-right: 10px;
  }
  .season-banner__text .hi { color: var(--yellow); font-weight: 600; }
  .season-banner__text .big {
    color: var(--yellow);
    font-size: 100px;
    font-weight: 400;
    line-height: 1;
    margin-right: 16px;
    position: relative;
    top: 4px;
  }
  .price-badge {
    position: absolute;
    left: 21px;
    top: 578px;
    width: 412px;
    height: 357px;
  }
  .price-badge svg { position: absolute; inset: 0; }
  .price-badge__text {
    position: absolute;
    inset: 0;
    text-align: center;
    color: var(--white);
  }
  .price-badge__label {
    position: absolute; left: 0; right: 0; top: 30px;
    color: var(--yellow); font-weight: 600; font-size: 50px; line-height: 1;
  }
  .price-badge__from {
    position: absolute; left: 0; right: 0; top: 80px;
    font-size: 40px; line-height: 1;
  }
  .price-badge__amount {
    position: absolute; left: 0; right: 0; top: 118px;
    color: var(--yellow); font-weight: 500; font-size: 165px; line-height: 1; letter-spacing: -4px;
  }
  .price-badge__unit {
    position: absolute; left: 0; right: 0; top: 293px;
    font-size: 31px; line-height: 1;
  }
  .brand {
    position: absolute;
    left: 58px;
    top: 1022px;
    display: flex;
    align-items: center;
    gap: 20px;
  }
  .brand__mark {
    width: 72px; height: 72px; border-radius: 50%;
    background: var(--yellow);
  }
  .brand__name {
    color: var(--logo-grey);
    font-weight: 800;
    font-size: 40px;
    line-height: 44px;
    letter-spacing: -0.5px;
    text-transform: uppercase;
  }
  .contact {
    position: absolute;
    right: 88px;
    top: 972px;
    text-align: right;
  }
  .contact__web {
    color: var(--white);
    font-size: 41px;
    line-height: 1;
    letter-spacing: 0.5px;
  }
  .contact__web .hi { color: var(--yellow); }
  .contact__phone {
    display: flex;
    align-items: center;
    justify-content: flex-end;
    gap: 26px;
    margin-top: 14px;
  }
  .contact__phone-number {
    color: var(--yellow);
    font-weight: 500;
    font-size: 84px;
    line-height: 1;
  }
  .footnote {
    position: absolute;
    left: 0; right: 0;
    top: 1152px;
    margin: 0;
    text-align: center;
    font-family: "Arimo", sans-serif;
    color: var(--yellow);
    font-size: 27px;
  }
</style>
</head>
<body>
<main class="sign">
  <svg class="sign__shapes" width="1200" height="1200" viewBox="0 0 1200 1200" aria-hidden="true">
    <polygon class="band-top" points="0,0 1200,0 1200,182 0,424" fill="#0b72bf"/>
    <polygon class="band-stripe" points="1200,180 1200,228 706,311 0,424" fill="#0a4fa6"/>
    <polygon class="band-wedge" points="706,311 1200,228 1200,411" fill="#343436"/>
    <polygon class="band-bottom" points="0,979 1200,863 1200,1200 0,1200" fill="#343436"/>
  </svg>

  <div class="heli-photo" role="img" aria-label="Photo of a red helicopter in flight against a blue sky"></div>

  <h1 class="headline">Helicopter Joy Flights<br>&amp; Scenic Tours</h1>

  <div class="season-banner">
    <svg width="950" height="131" viewBox="0 0 950 131" aria-hidden="true">
      <polygon points="28,0 922,0 950,30 950,101 922,131 28,131 0,101 0,30" fill="#0b72bf"/>
      <polygon points="36,12 914,12 938,36 938,95 914,119 36,119 12,95 12,36" fill="none" stroke="#ffffff" stroke-width="2"/>
    </svg>
    <p class="season-banner__text"><span class="big">7</span><span class="hi">Days</span>&nbsp;from&nbsp;<span class="hi">October</span>&nbsp;to&nbsp;<span class="hi">March.</span></p>
  </div>

  <div class="price-badge">
    <svg width="412" height="357" viewBox="0 0 412 357" aria-hidden="true">
      <polygon points="96,0 316,0 412,178 316,357 96,357 0,178" fill="#0b72bf"/>
      <polygon points="104,13 308,13 397,178 308,344 104,344 15,178" fill="none" stroke="#ffffff" stroke-width="2"/>
    </svg>
    <div class="price-badge__text">
      <span class="price-badge__label">Prices</span>
      <span class="price-badge__from">from just</span>
      <span class="price-badge__amount">$99</span>
      <span class="price-badge__unit">per person*</span>
    </div>
  </div>

  <div class="brand">
    <span class="brand__mark" aria-hidden="true"></span>
    <span class="brand__name">Skyquilla<br>Helicopters</span>
  </div>

  <div class="contact">
    <div class="contact__web">www.<span class="hi">skyquilla</span>.com.au</div>
    <div class="contact__phone">
      <svg width="72" height="72" viewBox="0 0 72 72" aria-hidden="true">
        <circle cx="36" cy="36" r="32" fill="none" stroke="#ffffff" stroke-width="4"/>
        <path d="M25 19 l7 9 -4 4 c2 5 6 9 11 11 l4 -4 9 7 -4 6 c-13 1 -28 -14 -28 -28 z" fill="none" stroke="#ffffff" stroke-width="3.5" stroke-linejoin="round"/>
        <path d="M40 22 a10 10 0 0 1 10 10 M40 14 a18 18 0 0 1 18 18" fill="none" stroke="#ffffff" stroke-width="3" stroke-linecap="round"/>
      </svg>
      <span class="contact__phone-number">9627 3105</span>
    </div>
  </div>

  <p class="footnote">* $99 flights are shared 8 minute flights and are only available on weekends</p>
</main>
</body>
</html>
```